Business Card Design

I would like a logo created for the top left corner of the card please. I would like a checkerboard in a dark navy with the edges fading out and one random bright orange square.
Updates

I have attached some further notes and a really rough sketch of what I am after.  Thank you. :)

Target Market(s)

Construction, mining, mechanical

Industry/Entity Type

Business

Contact Information for Business Card

Korvane Works Pty Ltd, Glen Hadwick, P. 0418365072, F. 0736209158, E.glen@korvaneworks.com.au, PO Box 87 YARRAWONGA Q 4581, ABN 53209874611

Font styles to use
Sans Serif

Requirements
Must have
• Really Dark Navy
Really bright Orange

```html
<!DOCTYPE html>
<html lang="en">
<head>
<meta charset="utf-8">
<title>Korvane Works Pty Ltd – Business Card</title>
<link href="https://fonts.googleapis.com/css2?family=Open+Sans:wght@400;600;700&display=swap" rel="stylesheet">
<style>
  :root {
    --stage: #4a4a4a;
    --stage-edge: #2e2e2e;
    --paper: #ffffff;
    --paper-shade: #eeeeee;
    --ink: #111111;
    --orange-top: #f7a028;
    --orange-bottom: #ef6629;
    --navy: #0d0f3a;
    --navy-mid: #1b2a8a;
    --cyan: #1ea8e0;
    --tile-grey: #e6e7ea;
  }
  * { box-sizing: border-box; margin: 0; padding: 0; }
  html, body { width: 1200px; height: 999px; overflow: hidden; }
  body {
    background: radial-gradient(ellipse at center, var(--stage) 0%, var(--stage-edge) 100%);
    font-family: "Open Sans", sans-serif;
    color: var(--ink);
    position: relative;
  }
  .card {
    position: absolute;
    left: 75px; top: 199px;
    width: 1050px; height: 600px;
    background: var(--paper);
    box-shadow: 0 4px 14px rgba(0,0,0,.35);
    overflow: hidden;
  }
  .card__top {
    position: absolute; left: 0; top: 0; width: 100%; height: 346px;
    background: linear-gradient(to bottom, var(--paper-shade) 0%, var(--paper) 30%, var(--paper) 100%);
  }
  .brand-mark {
    position: absolute; left: 41px; top: 43px;
    width: 285px; height: 214px;
    background:
      linear-gradient(to bottom, rgba(230,231,234,0) 0%, rgba(230,231,234,.35) 100%),
      linear-gradient(to bottom, var(--navy) 0%, var(--navy-mid) 55%, var(--cyan) 100%);
  }
  .company {
    position: absolute; right: 68px; top: 92px;
    text-align: right; font-weight: 600; color: var(--ink); line-height: 1.05;
  }
  .company__main { display: block; font-size: 64px; letter-spacing: -0.5px; }
  .company__suffix { display: block; font-size: 48px; margin-top: 6px; }
  .rule {
    position: absolute; left: 0; top: 348px; width: 100%; height: 9px;
    background: var(--ink);
  }
  .card__band {
    position: absolute; left: 0; top: 364px; width: 100%; height: 236px;
    background: linear-gradient(to bottom, var(--orange-top), var(--orange-bottom));
  }
  .band__notch { position: absolute; left: 0; top: 55px; }
  .person { position: absolute; left: 139px; top: 60px; }
  .person__name { font-size: 44px; font-weight: 700; line-height: 1.1; }
  .person__phone { font-size: 26px; margin-top: 8px; }
  .band__divider { position: absolute; left: 489px; top: 14px; }
  .details { position: absolute; left: 601px; top: 10px; font-size: 25px; line-height: 34px; }
  .details__line { display: block; }
  .contact { list-style: none; margin-top: 10px; }
  .contact__item { display: flex; align-items: center; height: 42px; }
  .contact__icon { width: 26px; height: 26px; margin-right: 21px; }
</style>
</head>
<body>
  <main class="card">
    <section class="card__top">
      <div class="brand-mark" role="img" aria-label="Company logo mark: navy checkerboard with one orange square"></div>
      <h1 class="company">
        <span class="company__main">Korvane Works</span>
        <span class="company__suffix">Pty Ltd</span>
      </h1>
    </section>
    <div class="rule"></div>
    <section class="card__band">
      <svg class="band__notch" width="60" height="120" viewBox="0 0 60 120" aria-hidden="true">
        <polygon points="0,0 59,60 0,120" fill="#ffffff"/>
      </svg>
      <div class="person">
        <h2 class="person__name">Glen Hadwick</h2>
        <p class="person__phone">0418 365 072</p>
      </div>
      <svg class="band__divider" width="6" height="206" viewBox="0 0 6 206" aria-hidden="true">
        <polygon points="3,0 5,103 3,206 1,103" fill="#111111"/>
      </svg>
      <div class="details">
        <span class="details__line">PO Box 87 YARRAWONGA Q 4581</span>
        <span class="details__line">ABN 53 209 874 611</span>
        <ul class="contact">
          <li class="contact__item">
            <svg class="contact__icon" viewBox="0 0 24 24" aria-label="Phone">
              <path d="M6.6 10.8a15 15 0 0 0 6.6 6.6l2.2-2.2a1 1 0 0 1 1-.25 11.4 11.4 0 0 0 3.6.57 1 1 0 0 1 1 1V20a1 1 0 0 1-1 1A17 17 0 0 1 3 4a1 1 0 0 1 1-1h3.5a1 1 0 0 1 1 1c0 1.250.2 2.450.57 3.57a1 1 0 0 1-.25 1z" fill="#111"/>
            </svg>
            <span>0418 365 072</span>
          </li>
          <li class="contact__item">
            <svg class="contact__icon" viewBox="0 0 24 24" aria-label="Fax">
              <rect x="7" y="2" width="10" height="7" fill="#111"/>
              <rect x="3" y="10" width="18" height="9" rx="1" fill="#111"/>
              <rect x="7" y="13" width="10" height="2" fill="#f3872a"/>
              <rect x="2" y="20" width="20" height="2" fill="#111"/>
            </svg>
            <span>07 3620 9158</span>
          </li>
          <li class="contact__item">
            <svg class="contact__icon" viewBox="0 0 24 24" aria-label="Email">
              <path d="M2 9l10-6 10 6v12H2z" fill="#111"/>
              <path d="M5 10l7 5 7-5" fill="none" stroke="#f0702a" stroke-width="1.6"/>
            </svg>
            <span>glen@korvaneworks.com.au</span>
          </li>
        </ul>
      </div>
    </section>
  </main>
</body>
</html>
```